(2) Graphics for Online Store. Creative Minds Welcome+

Need (2) Different Graphics for an Online Store selling digital goods.

The digital goods are 'Leads' for Business Loan Brokers. The graphic should resemble 'Money' in some creative way.

#1 Aged Business Funding Leads
# 2 'Business Funding Real Time Calls

Preferred Colors: White/Black/Aqua

Examples of each included below. Not looking for replicas. The attached are examples of similar products only. No Clipart Please! Needs to be a Professional Clean Look! Do not replicate or emulate the attached. This is just an example.

```html
<!DOCTYPE html>
<html lang="en">
<head>
<meta charset="utf-8">
<title>Aged Business Loan Leads</title>
<link rel="stylesheet" href="https://fonts.googleapis.com/css2?family=Roboto+Slab:wght@300;400;800;900&display=swap">
<style>
  :root {
    --aqua: #2ac7ad;
    --aqua-deep: #1fb59c;
    --aqua-light: #46d5bd;
    --ink: #050505;
    --white: #ffffff;
    --suit: #1e2226;
  }
  html, body {
    margin: 0;
    padding: 0;
    width: 1200px;
    height: 675px;
    overflow: hidden;
    background: var(--aqua);
  }
  .store-graphic {
    display: block;
    width: 1200px;
    height: 675px;
    font-family: "Roboto Slab", Georgia, serif;
  }
  .headline-light { font-weight: 300; fill: var(--ink); }
  .headline-heavy { font-weight: 900; fill: var(--ink); }
  .badge-text { font-weight: 800; fill: var(--aqua); }
  .badge-text--light { font-weight: 400; }
  .tag-text { font-weight: 800; fill: var(--aqua); }
  .product-line { font-weight: 900; fill: var(--ink); }
</style>
</head>
<body>
<svg class="store-graphic" viewBox="0 0 1200 675" xmlns="http://www.w3.org/2000/svg">
  <defs>
    <linearGradient id="bg-money" x1="0" y1="0" x2="1" y2="1">
      <stop offset="0" stop-color="#46d5bd"/>
      <stop offset="0.5" stop-color="#2ac7ad"/>
      <stop offset="1" stop-color="#1fb59c"/>
    </linearGradient>
    <linearGradient id="broker-tone" x1="0" y1="0" x2="0" y2="1">
      <stop offset="0" stop-color="#8a6a52"/>
      <stop offset="0.3" stop-color="#2a2d31"/>
      <stop offset="1" stop-color="#1e2226"/>
    </linearGradient>
  </defs>

  <rect class="money-backdrop" role="img" aria-label="Faint scattered dollar bills tinted aqua" x="0" y="0" width="1200" height="675" fill="url(#bg-money)"/>

  <rect class="broker-photo" role="img" aria-label="Smiling bearded broker in a dark suit holding a wallet full of cash" x="30" y="25" width="362" height="650" rx="40" fill="url(#broker-tone)"/>

  <g class="age-badge">
    <polygon points="1058,247 1176,339 1155,487 1016,544 898,451 919,303" fill="var(--white)"/>
    <polygon points="1057,260 1164,343 1145,477 1017,530 910,447 929,313" fill="none" stroke="var(--aqua)" stroke-width="5"/>
  </g>

  <g class="headline">
    <text class="headline-light" x="457" y="90" font-size="66" textLength="447" lengthAdjust="spacingAndGlyphs">COMISSION</text>
    <text class="headline-heavy" x="457" y="202" font-size="124" textLength="526" lengthAdjust="spacingAndGlyphs">MONEY</text>
    <text class="headline-light" x="457" y="281" font-size="78" textLength="549" lengthAdjust="spacingAndGlyphs">JUST WAITING</text>
    <text class="headline-light" x="457" y="369" font-size="62" textLength="228" lengthAdjust="spacingAndGlyphs">TO BE</text>
    <text class="headline-heavy" x="457" y="487" font-size="136" textLength="478" lengthAdjust="spacingAndGlyphs">FOUND</text>
  </g>

  <g class="age-badge-text" text-anchor="middle">
    <text class="badge-text" x="1017" y="348" font-size="46" textLength="101" lengthAdjust="spacingAndGlyphs">10+</text>
    <text class="badge-text" x="1037" y="413" font-size="48" textLength="149" lengthAdjust="spacingAndGlyphs">DAYS</text>
    <text class="badge-text badge-text--light" x="1044" y="470" font-size="50" textLength="158" lengthAdjust="spacingAndGlyphs">AGED</text>
  </g>

  <g class="quantity-tag">
    <rect x="376" y="537" width="313" height="56" rx="6" fill="var(--ink)"/>
    <text class="tag-text" x="421" y="580" font-size="38" textLength="248" lengthAdjust="spacingAndGlyphs">100 LEADS</text>
  </g>

  <text class="product-line" x="426" y="637" font-size="44" textLength="698" lengthAdjust="spacingAndGlyphs">AGED BUSINESS LOAN LEADS</text>
</svg>
</body>
</html>
```